Business Cards for a Junk Removal Company

Hello,
We are looking to have business cards designed that are simple, bold, easy to read, and right to the point. Please see the attachments for our logo files. We want the card to be yellow on both sides ( Color code Yellow: #FFE01B). The logo text font is (Rockstar Extra Bold) and this is also in the files attached. Please make the text black for the logo. On the back side of the card, you can use white and black for text. Thank you in advance for your hard work!

Front of card-
Harbor Haul Away (logo)
Back of card-
Harbor Haul Away
Donate - Recycle - Dispose
555-271-8093
www.harborhaulaway.example
info@harborhaulaway.example

Industry/Entity Type

Junk removal

Contact Information for Business Card

FRONT OF CARD- Harbor Haul Away (logo) BACK OF CARD- Harbor Haul Away Donate - Recycle - Dispose 555-271-8093 www.harborhaulaway.example info@harborhaulaway.example

Font styles to use
Other font styles liked:
• Rockstar Extra Bold

Colors
FFF300
FFF600
FEFA6F
FFFEC7
FFFEE8

Requirements
Must have
• Must have color code Yellow: #FFE01B for the background of front and back of the card

```html
<!DOCTYPE html>
<html lang="en">
<head>
<meta charset="utf-8">
<title>Harbor Haul Away – Business Cards</title>
<link href="https://fonts.googleapis.com/css2?family=Anton&display=swap" rel="stylesheet">
<style>
  :root {
    --stage: #969696;
    --card-yellow: #FFE01B;
    --ink: #0a0a0a;
  }
  * { margin: 0; padding: 0; box-sizing: border-box; }
  html, body { width: 1200px; height: 1000px; overflow: hidden; }
  body {
    background: var(--stage);
    position: relative;
    font-family: "Anton", "Arial Narrow", sans-serif;
    color: var(--ink);
  }
  .card {
    position: absolute;
    top: 193px;
    width: 351px;
    height: 614px;
    background: var(--card-yellow);
  }
  .card--front { left: 184px; }
  .card--back { left: 605px; }

  .brand-name {
    position: absolute;
    left: 0; right: 0;
    text-align: center;
    text-transform: uppercase;
    font-size: 56px;
    line-height: 1.02;
    letter-spacing: 1px;
    color: var(--ink);
  }
  .card--front .brand-name { top: 250px; }
  .card--back .brand-name { top: 488px; font-size: 48px; }

  .services {
    position: absolute;
    left: 20px;
    top: 40px;
    list-style: none;
  }
  .service {
    display: flex;
    align-items: center;
    height: 72px;
  }
  .service-icon {
    width: 54px;
    height: 54px;
    margin-right: 14px;
    flex: none;
  }
  .service-label {
    font-size: 66px;
    line-height: 1;
    text-transform: uppercase;
    letter-spacing: 1px;
  }

  .contact {
    position: absolute;
    left: 20px;
    right: 18px;
    top: 310px;
    text-transform: uppercase;
  }
  .contact-phone {
    font-size: 48px;
    line-height: 1;
    letter-spacing: 2px;
  }
  .contact-web, .contact-email {
    font-size: 22px;
    line-height: 1.2;
    letter-spacing: 0.5px;
    margin-top: 2px;
  }
  .contact-email { font-size: 20px; }
</style>
</head>
<body>

  <section class="card card--front" aria-label="Card front">
    <h1 class="brand-name">Harbor<br>Haul Away</h1>
  </section>

  <section class="card card--back" aria-label="Card back">
    <ul class="services">
      <li class="service">
        <svg class="service-icon" viewBox="0 0 54 54" aria-hidden="true">
          <path d="M27 30 C17 22 14 18 16 13 C18 8 24 8 27 13 C30 8 36 8 38 13 C40 18 37 22 27 30 Z" fill="var(--ink)"/>
          <rect x="2" y="34" width="8" height="14" fill="var(--ink)"/>
          <path d="M12 35 H28 C32 35 32 40 28 40 H20 M12 47 H30 L50 37 C53 35 51 31 47 33 L34 39" fill="none" stroke="var(--ink)" stroke-width="4" stroke-linejoin="round"/>
        </svg>
        <span class="service-label">Donate</span>
      </li>
      <li class="service">
        <svg class="service-icon" viewBox="0 0 54 54" aria-hidden="true">
          <g fill="none" stroke="var(--ink)" stroke-width="6">
            <path d="M16 22 L24 8 H32 L38 18"/>
            <path d="M44 28 L48 36 L44 44 H32"/>
            <path d="M20 44 H10 L6 36 L12 26"/>
          </g>
          <g fill="var(--ink)">
            <path d="M33 20 L44 22 L42 11 Z"/>
            <path d="M34 36 L26 44 L34 52 Z"/>
            <path d="M4 26 L16 21 L18 32 Z"/>
          </g>
        </svg>
        <span class="service-label">Recycle</span>
      </li>
      <li class="service">
        <svg class="service-icon" viewBox="0 0 54 54" aria-hidden="true">
          <rect x="20" y="2" width="14" height="5" fill="var(--ink)"/>
          <rect x="10" y="7" width="34" height="6" fill="var(--ink)"/>
          <path d="M13 16 H41 L38 52 H16 Z" fill="var(--ink)"/>
          <g stroke="var(--card-yellow)" stroke-width="2.5">
            <line x1="20" y1="21" x2="21" y2="47"/>
            <line x1="27" y1="21" x2="27" y2="47"/>
            <line x1="34" y1="21" x2="33" y2="47"/>
          </g>
        </svg>
        <span class="service-label">Dispose</span>
      </li>
    </ul>

    <div class="contact">
      <p class="contact-phone">555-271-8093</p>
      <p class="contact-web">www.harborhaulaway.example</p>
      <p class="contact-email">info@harborhaulaway.example</p>
    </div>

    <p class="brand-name">Harbor<br>Haul Away</p>
  </section>

</body>
</html>
```